Help a start up law firm make an impression! - Website

We are a property development and conveyancing law firm looking for some to design our website. The initial brief is for 6 pages with scope for on-going work.

Law firms are traditionally quite conservative and we want to break the mold. We want to come across as fun and modern, while still being professional.

A good example is https://quorvantlaw.com.au/. It's professional yet modern.
Updates

Another good site I like in the same industry: https://www.tamberwickconveyancing.com.au/

Target Market(s)

Tech savy home buyers and sellers - generally 30 to 50 years old

Industry/Entity Type

Law Firm

Coding

Coded - Design and coding required

Number of Pages Required

5+ page

Font styles to use
Other font styles liked:
• No idea

Colors
f04a50

Requirements
Must have
• The elements set out in the design brief document

```html
<!DOCTYPE html>
<html lang="en">
<head>
<meta charset="utf-8">
<title>Kellaway Law — The Property Law Experts</title>
<link href="https://fonts.googleapis.com/css2?family=Montserrat:wght@400;500;600;700&family=Open+Sans:wght@400;600;700&display=swap" rel="stylesheet">
<style>
:root{
  --brand:#d63f5f;
  --brand-dark:#cc3a58;
  --brand-light:#e95f7b;
  --blush:#fde9ef;
  --blush-deep:#f9d9e3;
  --ink:#222;
  --text:#333;
  --muted:#666;
  --footer-dark:#2d2d2d;
  --white:#fff;
}
*{box-sizing:border-box;margin:0;padding:0}
html,body{width:1200px;height:3409px;overflow:hidden}
body{font-family:"Open Sans",Arial,sans-serif;color:var(--text);background:var(--white);position:relative}
.heading-font{font-family:"Montserrat",Arial,sans-serif}

/* Header */
.site-header{position:absolute;top:0;left:0;width:1200px;height:75px;background:var(--white);display:flex;align-items:center;padding:0 52px}
.brand-name{font-family:"Montserrat",Arial,sans-serif;font-weight:700;font-size:31px;color:var(--ink);letter-spacing:-.5px}
.header-actions{margin-left:auto;display:flex;align-items:center;gap:32px;font-family:"Montserrat",Arial,sans-serif;font-weight:700;font-size:18px}
.call{display:flex;align-items:center;gap:10px;color:var(--ink)}
.menu{display:flex;align-items:center;gap:8px;color:var(--brand)}

/* Hero */
.hero{position:absolute;top:75px;left:0;width:1200px;height:557px;background:linear-gradient(180deg,#3a3a3a 0%,#2a2a2a 45%,#1e1e1e 70%,#353535 100%);text-align:center;color:var(--white)}
.hero h1{font-family:"Montserrat",Arial,sans-serif;font-weight:700;font-size:36px;margin-top:135px;letter-spacing:.3px}
.hero p{font-family:"Montserrat",Arial,sans-serif;font-weight:700;font-size:26px;line-height:38px;margin-top:30px}
.btn{display:inline-flex;align-items:stretch;background:var(--brand);color:var(--white);font-family:"Montserrat",Arial,sans-serif;font-size:11px;font-weight:500;text-transform:uppercase;height:40px;line-height:40px}
.btn .arrow{width:34px;display:flex;align-items:center;justify-content:center;border-left:1px solid rgba(255,255,255,.35)}
.btn .arrow.first{border-left:none;border-right:1px solid rgba(255,255,255,.35)}
.btn .label{padding:0 24px}
.hero .btn{margin-top:44px}
.to-top{position:absolute;right:34px;top:465px;width:32px;height:28px;background:rgba(255,255,255,.15);display:flex;align-items:center;justify-content:center}

/* Features */
.features{position:absolute;top:632px;left:0;width:1200px;height:391px;display:flex}
.feature{width:300px;height:100%;text-align:center;color:var(--white);padding:40px 24px 0}
.feature:nth-child(odd){background:var(--brand-dark)}
.feature:nth-child(even){background:var(--brand-light)}
.feature .icon{width:78px;height:78px;border-radius:50%;background:var(--white);margin:0 auto;display:flex;align-items:center;justify-content:center}
.feature h3{font-family:"Montserrat",Arial,sans-serif;font-weight:500;font-size:16px;margin-top:22px;text-transform:uppercase}
.feature p{font-size:13px;line-height:20px;margin-top:14px}

/* Service rows */
.service{position:absolute;left:0;width:1200px}
.service-conveyancing{top:1023px;height:409px;background:var(--white)}
.service-development{top:1432px;height:414px;background:var(--blush)}
.photo{position:absolute;box-shadow:0 4px 10px rgba(0,0,0,.3)}
.service h2{font-family:"Montserrat",Arial,sans-serif;font-weight:400;font-size:26px;color:var(--ink);position:absolute}
.service h2 strong,.section-title strong{color:var(--brand);font-weight:600}
.service p{position:absolute;font-size:13px;line-height:21px;color:var(--text)}
.service .btn{position:absolute;height:36px;line-height:36px}

/* Articles */
.articles{position:absolute;top:1846px;left:0;width:1200px;height:666px}
.section-title{font-family:"Montserrat",Arial,sans-serif;font-weight:400;font-size:26px;color:var(--ink);text-align:center}
.articles .section-title{margin-top:80px}
.article{position:absolute;top:168px;width:345px}
.article .thumb{height:229px}
.article h4{font-family:"Open Sans",Arial,sans-serif;font-weight:400;font-size:11px;color:var(--muted);margin-top:22px}
.article p{font-size:13px;line-height:21px;margin-top:4px;color:var(--ink)}

/* Contact */
.contact{position:absolute;top:2512px;left:0;width:1200px;height:541px;background:linear-gradient(180deg,#fbe3ea 0%,#f8dbe4 50%,#fbe6ec 100%)}
.contact .section-title{margin-top:78px}
.contact-form{position:absolute;left:268px;top:170px;width:650px}
.field-row{display:flex;gap:24px;margin-bottom:16px}
.field{flex:1;height:26px;background:var(--white);border:1px solid #e2c5cd;font-size:10px;color:#aaa;padding:5px 8px}
.field.message{height:135px;margin-bottom:38px}
.submit{height:39px;background:var(--brand);color:var(--white);font-family:"Montserrat",Arial,sans-serif;font-size:11px;text-align:center;line-height:39px;text-transform:uppercase}

/* Footer */
.footer-rule{position:absolute;top:3053px;left:0;width:1200px;height:11px;background:var(--brand)}
.site-footer{position:absolute;top:3064px;left:0;width:1200px;height:245px;background:var(--white)}
.footer-col{position:absolute;top:44px}
.footer-col h5{font-family:"Montserrat",Arial,sans-serif;font-weight:700;font-size:17px;color:var(--brand);text-transform:uppercase;margin-top:8px}
.footer-col ul{list-style:none;margin-top:30px;font-size:13px;line-height:21px;color:var(--ink)}
.footer-about p{font-size:13px;line-height:21px;color:var(--ink);margin-top:40px;width:345px}
.legal-bar{position:absolute;top:3309px;left:0;width:1200px;height:100px;background:var(--footer-dark);color:#ddd;text-align:center;font-size:10px;line-height:20px;padding-top:34px;text-transform:uppercase}
</style>
</head>
<body>

<header class="site-header">
  <div class="brand-name">Kellaway Law</div>
  <div class="header-actions">
    <div class="call">
      <svg width="17" height="17" viewBox="0 0 24 24"><path fill="#222" d="M6.6 10.8a15.1 15.1 0 0 0 6.6 6.6l2.2-2.2c.3-.3.7-.4 1-.2 1.1.4 2.3.6 3.6.6.6 0 1 .4 1 1V20c0 .6-.4 1-1 1C10.6 21 3 13.4 3 4c0-.6.4-1 1-1h3.5c.6 0 1 .4 1 1 0 1.3.2 2.5.6 3.6.1.3 0 .7-.2 1z"/></svg>
      <span>Call Us: 07 3900 4821</span>
    </div>
    <div class="menu">
      <svg width="16" height="14" viewBox="0 0 16 14"><rect width="16" height="2.5" fill="#d63f5f"/><rect y="5.7" width="16" height="2.5" fill="#d63f5f"/><rect y="11.5" width="16" height="2.5" fill="#d63f5f"/></svg>
      <span>Menu</span>
    </div>
    <svg width="18" height="18" viewBox="0 0 20 20"><circle cx="8" cy="8" r="6" fill="none" stroke="#222" stroke-width="2.6"/><line x1="12.5" y1="12.5" x2="18" y2="18" stroke="#222" stroke-width="2.8"/></svg>
  </div>
</header>

<section class="hero" role="img" aria-label="Night view of a city skyline and river bridge, darkened behind the headline">
  <h1>THE PROPERTY LAW EXPERTS</h1>
  <p>Unrivaled response times,<br>fixed fee options and experienced<br>property lawyers</p>
  <a class="btn"><span class="label">Contact Us</span><span class="arrow">»</span></a>
  <div class="to-top"><svg width="12" height="8" viewBox="0 0 12 8"><path d="M1 7l5-5 5 5" fill="none" stroke="#fff" stroke-width="1.6"/></svg></div>
</section>

<section class="features">
  <div class="feature">
    <div class="icon"><svg width="40" height="40" viewBox="0 0 40 40"><text x="20" y="31" text-anchor="middle" font-family="Montserrat, Arial, sans-serif" font-weight="700" font-size="32" fill="#222">$</text></svg></div>
    <h3>Cost Certainty</h3>
    <p>Flexible fee arrangements with no surprises. We offer fixed fee, pay on completion and monthly retainer options to suit your needs.</p>
  </div>
  <div class="feature">
    <div class="icon"><svg width="46" height="40" viewBox="0 0 46 40" fill="none" stroke="#222" stroke-width="2.4"><line x1="23" y1="4" x2="23" y2="34"/><line x1="8" y1="9" x2="38" y2="9"/><line x1="14" y1="35" x2="32" y2="35"/><path d="M8 9l-6 14h12z"/><path d="M38 9l-6 14h12z"/><path d="M2 23a6 5 0 0 0 12 0"/><path d="M32 23a6 5 0 0 0 12 0"/></svg></div>
    <h3>Expert Lawyers</h3>
    <p>Our experienced team has managed over 2,000 conveyances and worked on some of the most iconic developments in Queensland. All we do is property law, all day everyday.</p>
  </div>
  <div class="feature">
    <div class="icon"><svg width="40" height="40" viewBox="0 0 40 40"><circle cx="20" cy="20" r="15" fill="none" stroke="#222" stroke-width="4"/><path d="M20 11v10h7" fill="none" stroke="#222" stroke-width="3"/></svg></div>
    <h3>Responsive Services</h3>
    <p>The most responsive service, guaranteed. No more waiting days for a lawyer to respond to your email, return your call or prepare your contract.</p>
  </div>
  <div class="feature">
    <div class="icon"><svg width="48" height="36" viewBox="0 0 48 36" fill="none" stroke="#222" stroke-width="2.6" stroke-linejoin="round"><path d="M2 10l8-4 6 14-8 4z" fill="#222"/><path d="M46 10l-8-4-6 14 8 4z" fill="#222"/><path d="M14 9l8-3 6 3 8-1 4 12-10 9-4-3-4 2-8-7"/><path d="M22 16l6-3 8 8"/></svg></div>
    <h3>Commercial Advice</h3>
    <p>We work with you to get the deal done without legal jargon getting in the way. We understand timing is crucial and we focus on the legal issues that are important to you.</p>
  </div>
</section>

<section class="service service-conveyancing">
  <div class="photo" role="img" aria-label="Keys resting on a signed property contract" style="left:52px;top:88px;width:346px;height:230px;background:linear-gradient(135deg,#c9d3de 0%,#9aa9b8 55%,#d6dde5 100%)"></div>
  <h2 style="left:441px;top:96px">Conveyancing <strong>Services</strong></h2>
  <p style="left:441px;top:150px;width:705px">Lorem ipsum dolor sit amet, consectetur adipiscing elit. Integer et urna ac lorem efficitur faucibus. In faucibus pulvinar lacus, consectetur gravida quam ultricies non. Maecenas sed odio a leo iaculis tempus. Nam dignissim felis neque, sit amet ullamcorper enim ornare ut. Duis commodo purus eu pellentesque feugiat.Lorem ipsum dolor sit amet, consectetur adipiscing elit. Integer et urna ac lorem efficitur faucibus. Duis commodo purus eu pellentesque feugiat.</p>
  <a class="btn" style="left:441px;top:286px"><span class="arrow first">»</span><span class="label">Read More</span></a>
</section>

<section class="service service-development">
  <h2 style="left:52px;top:94px">Property <strong>Development</strong></h2>
  <p style="left:52px;top:152px;width:700px">Lorem ipsum dolor sit amet, consectetur adipiscing elit. Integer et urna ac lorem efficitur faucibus. In faucibus pulvinar lacus, consectetur gravida quam ultricies non. Maecenas sed odio a leo iaculis tempus. Nam dignissim felis neque, sit amet ullamcorper enim ornare ut. Duis commodo purus eu pellentesque feugiat.Lorem ipsum dolor sit amet, consectetur adipiscing elit. Integer et urna ac lorem efficitur faucibus. Duis commodo purus eu pellentesque feugiat.</p>
  <a class="btn" style="left:52px;top:289px"><span class="arrow first">»</span><span class="label">Read More</span></a>
  <div class="photo" role="img" aria-label="Business meeting over documents with a small model house" style="left:786px;top:91px;width:348px;height:232px;background:linear-gradient(135deg,#e9eef2 0%,#b8c6cf 50%,#7f96a3 100%)"></div>
</section>

<section class="articles">
  <h2 class="section-title">Latest <strong>Articles</strong></h2>
  <article class="article" style="left:52px">
    <div class="thumb" role="img" aria-label="Silhouettes of business people by tall office windows" style="background:linear-gradient(160deg,#9cc3e8 0%,#3f78b4 55%,#1c3e6b 100%)"></div>
    <h4>Real estate laws on the move</h4>
    <p>Lorem Ipsum is simply dummy text of the printing and typesetting industry. Lorem Ipsum has been the industry's standard dummy text ever since the 1500s, when an unknown printer took a galley of type and [...]</p>
  </article>
  <article class="article" style="left:420px">
    <div class="thumb" role="img" aria-label="Business people talking outside a glass office building" style="background:linear-gradient(170deg,#dfe8f0 0%,#a9bccb 50%,#4a5563 100%)"></div>
    <h4>Private equity firm takes control</h4>
    <p>Lorem Ipsum is simply dummy text of the printing and typesetting industry. Lorem Ipsum has been the industry's standard dummy text ever since the 1500s, when an unknown printer took a galley of type and [...]</p>
  </article>
  <article class="article" style="left:789px">
    <div class="thumb" role="img" aria-label="Colleagues gathered around a laptop in an office" style="background:linear-gradient(150deg,#6b4a38 0%,#a78466 50%,#d9c8b4 100%)"></div>
    <h4>Tax litigation at your door</h4>
    <p>Lorem Ipsum is simply dummy text of the printing and typesetting industry. Lorem Ipsum has been the industry's standard dummy text ever since the 1500s, when an unknown printer took a galley of type and [...]</p>
  </article>
</section>

<section class="contact" role="img" aria-label="Faint pink-tinted collage of smiling clients behind the contact form">
  <h2 class="section-title">Get in <strong>Touch</strong></h2>
  <form class="contact-form">
    <div class="field-row"><div class="field">First Name</div><div class="field">Last Name</div></div>
    <div class="field-row"><div class="field">Email</div><div class="field">Phone</div></div>
    <div class="field message">Message</div>
    <div class="submit">Get in Touch</div>
  </form>
</section>

<div class="footer-rule"></div>
<footer class="site-footer">
  <div class="footer-col footer-about" style="left:52px">
    <div class="brand-name">Kellaway Law</div>
    <p>Kellaway Law is a specialised property development law firm established to assist small to medium property developers with their Queensland developments.</p>
  </div>
  <div class="footer-col" style="left:420px">
    <h5>Our Advantages</h5>
    <ul><li>Cost Certainty</li><li>The Property Law Experts</li><li>Responsive Services&gt;</li><li>Commercial Advice</li></ul>
  </div>
  <div class="footer-col" style="left:791px">
    <h5>Contact Us</h5>
    <ul><li>48 Harbour Lane Brisbane, QLD 4000</li><li>Phone: 0738004410</li><li>Mobile: 0738004410</li><li>Fax: 0738004410</li><li>Email: hello@kellawaylaw.com.au</li></ul>
  </div>
</footer>
<div class="legal-bar">Copyright 2017 Kellaway Law<br>Use of kellawaylaw.com.au is subject to our legal notices.</div>

</body>
</html>
```